Design some Business Cards for Velquira

Hi,

Need a new business card design for Velquira. Velquira is a boutique hair and beauty salon. Please find attached file for inspiration.

```html
<!DOCTYPE html>
<html lang="en">
<head>
<meta charset="utf-8">
<title>Velquira – Business Cards</title>
<link href="https://fonts.googleapis.com/css2?family=Arimo:wght@400;700&display=swap" rel="stylesheet">
<style>
  :root {
    --magenta: #c2186f;
    --ink: #1a1a1a;
    --paper: #ffffff;
    --skin-light: #f4e1d6;
    --skin-mid: #e2bda8;
    --lip: #b3121e;
  }
  * { box-sizing: border-box; margin: 0; padding: 0; }
  html, body {
    width: 1200px;
    height: 1200px;
    overflow: hidden;
    background: var(--paper);
    font-family: "Arimo", Arial, sans-serif;
  }
  .canvas {
    position: relative;
    width: 1200px;
    height: 1200px;
    background: var(--paper);
  }

  /* Back of card (magenta, tilted) */
  .card-back {
    position: absolute;
    left: 335px;
    top: 515px;
    width: 735px;
    height: 458px;
    background: var(--magenta);
    transform: rotate(-14deg);
    transform-origin: center;
    display: flex;
    align-items: center;
    justify-content: center;
  }
  .card-back .brand {
    color: var(--paper);
  }

  /* Front of card */
  .card-front {
    position: absolute;
    left: 77px;
    top: 147px;
    width: 747px;
    height: 424px;
    background: var(--paper);
  }
  .card-front .brand-area {
    position: absolute;
    left: 40px;
    top: 70px;
    width: 380px;
    height: 160px;
    display: flex;
    align-items: center;
  }
  .card-front .brand {
    color: var(--magenta);
  }
  .brand {
    display: flex;
    align-items: center;
    gap: 14px;
    font-family: "Arimo", Arial, sans-serif;
    font-weight: 700;
    font-size: 62px;
    letter-spacing: 1px;
    line-height: 1;
  }
  .brand-dot {
    width: 22px;
    height: 22px;
    border-radius: 50%;
    background: currentColor;
  }

  .contact {
    position: absolute;
    left: 28px;
    top: 316px;
    color: var(--ink);
    font-size: 17px;
    font-weight: 700;
    line-height: 19px;
  }
  .contact .email { font-weight: 400; font-weight: 700; }

  .base-band {
    position: absolute;
    left: 0;
    bottom: 0;
    width: 427px;
    height: 20px;
    background: var(--magenta);
  }

  .portrait {
    position: absolute;
    left: 427px;
    top: 0;
    width: 320px;
    height: 424px;
    background:
      radial-gradient(ellipse 40% 8% at 35% 56%, rgba(179,18,30,0.55), transparent 70%),
      linear-gradient(160deg, var(--paper) 0%, var(--skin-light) 35%, var(--skin-mid) 100%);
  }
</style>
</head>
<body>
  <main class="canvas">
    <section class="card-back" aria-label="Business card, back">
      <div class="brand">
        <span class="brand-dot"></span>
        <span class="brand-name">Velquira</span>
      </div>
    </section>

    <section class="card-front" aria-label="Business card, front">
      <div class="brand-area">
        <div class="brand">
          <span class="brand-dot"></span>
          <span class="brand-name">Velquira</span>
        </div>
      </div>

      <address class="contact">
        <div class="contact-name">Marissa Talbrook</div>
        <div class="contact-phone">0400 318 572</div>
        <div class="contact-email">hello@velquirahair.com</div>
        <div class="contact-address">28 Ellery Lane, Marrowvale Q 4702</div>
      </address>

      <div class="base-band"></div>

      <div class="portrait" role="img" aria-label="Close-up beauty photograph of a woman with red lipstick, hand resting at her cheek"></div>
    </section>
  </main>
</body>
</html>
```